Re-design my 1-page website to be BETTER!

Hi Guys,
I recently created a 1-page website for market testing purposes for a company I am starting. Problem is, the feedback i've had on the page is its a bit corporate and boring.
I would love you to design something that is fresher, more modern and will generate leads (via the sign up CTA's).
Here is the website as it is now: www.guidelinkhub.com.au.
If you need any info or have questions, just reach out.
Thanks,
Oliver

Target Market(s)

Entrepreneurs

Number of Pages Required

1 page

Font styles to use
Sans Serif

Colors
abd036
34a6d7
ffffff

Requirements
Must have
• Fresh, Modern, high-converting
• I expect 70% of traffic to be mobile so must be mobile optimised first.
Nice to have
• I've highlighted colours i like below, however, I am open to suggestions. I like colours that are gender neutral and show energy and vibrancy.
• I have used Proxima Nova for the fonts, as I find it easy to read however, I am open to suggestions. My main preference is that it displays well and is easily read

```html
<!DOCTYPE html>
<html lang="en">
<head>
<meta charset="utf-8">
<title>GuideLink Hub – A Mentor for Everyone</title>
<link rel="stylesheet" href="https://fonts.googleapis.com/css2?family=Poppins:ital,wght@0,300;0,400;0,500;1,300&display=swap">
<style>
:root{
  --blue:#34a6d7;
  --green:#abd036;
  --white:#ffffff;
  --ink:#3d3d3d;
  --body:#4a4a4a;
  --panel:#f4f4f4;
  --deep-blue:#2a7ea8;
  --deep-green:#8fb23a;
}
*{box-sizing:border-box;margin:0;padding:0}
html,body{width:1200px;height:4125px;overflow:hidden}
body{position:relative;background:var(--white);font-family:'Poppins',sans-serif;color:var(--body)}
.abs{position:absolute}
.center{text-align:center}
.btn{position:absolute;display:flex;align-items:center;justify-content:center;background:var(--blue);color:var(--white);border-radius:20px;font-size:10px;font-weight:500;box-shadow:0 2px 6px rgba(52,166,215,.35)}
.section-title{position:absolute;left:0;width:1200px;text-align:center;color:var(--blue);font-weight:500;font-size:27px}
.rule{position:absolute;left:576px;width:48px;height:4px;background:var(--green);border-radius:2px}
.rule.small{left:0;width:24px;height:3px}

/* hero */
.brand{left:211px;top:33px;font-size:19px;font-weight:500;color:var(--blue)}
.hero-photo{left:0;top:0;width:1200px;height:520px}
.hero-title{left:211px;top:224px;font-size:45px;font-weight:500;color:var(--ink);letter-spacing:-.5px}
.hero-sub{left:212px;top:278px;font-size:13px;color:var(--ink)}

/* quote */
.quote{left:330px;top:543px;width:540px;text-align:center;font-size:16px;font-style:italic;font-weight:300;line-height:23px;color:var(--ink)}
.quote-by{left:590px;top:628px;width:266px;text-align:right;font-size:15px;color:var(--blue)}

/* intro */
.intro-blob{left:430px;top:815px;width:330px;height:295px}
.intro-copy{left:270px;top:840px;width:660px;text-align:center;font-size:16px;line-height:23px;color:var(--ink)}
.intro-copy p{margin-bottom:23px}

/* steps */
.lead{left:330px;top:1292px;width:540px;text-align:center;font-size:16px;line-height:23px;color:var(--ink)}
.step{position:absolute;top:1483px;width:220px;text-align:center}
.step h3{font-size:15px;font-weight:500;color:var(--blue);margin-bottom:26px}
.step p{font-size:12.5px;line-height:18.7px;color:var(--ink)}

/* benefits */
.benefits{left:0;top:1870px;width:1200px;height:750px;clip-path:polygon(0 0,100% 0,100% 100%,0 92.4%);background:linear-gradient(100deg,#2f6f93 0%,#3b8a97 35%,#6b9f63 65%,#93b43c 100%)}
.benefits-title{left:0;top:1956px;width:1200px;text-align:center;color:var(--white);font-size:26px;font-weight:500}
.benefit{position:absolute;width:214px;text-align:center;color:var(--white)}
.benefit svg{display:block;margin:0 auto 10px;width:44px;height:44px}
.benefit h3{font-size:15px;font-weight:400;margin-bottom:12px}
.benefit .rule{position:relative;display:block;margin:0 auto 16px;width:24px;height:3px}
.benefit p{font-size:10px;line-height:15px}

/* faq */
.faq-item{position:absolute;left:211px;width:382px;height:48px;border:2px solid var(--green);border-radius:10px;padding-left:16px;display:flex;align-items:center;font-size:15px;color:var(--ink)}
.faq-item.active{background:var(--blue);border-color:var(--blue);color:var(--white)}
.faq-answer{left:607px;top:2877px;width:380px;height:401px;background:var(--panel);border-radius:10px;padding:31px 36px 0 32px;font-size:12.5px;line-height:18.5px;color:var(--ink)}
.faq-answer p{margin-bottom:18px}

/* cta */
.cta{left:0;top:3422px;width:1200px;height:500px;clip-path:polygon(0 0,100% 10.8%,100% 100%,0 100%);background:linear-gradient(100deg,#8fb33d 0%,#6ea463 40%,#3e90a2 75%,#2f83aa 100%)}
.cta-title{left:0;top:3536px;width:1200px;text-align:center;color:var(--white);font-size:27px;font-weight:500}
.cta-copy{left:340px;top:3621px;width:520px;text-align:center;color:var(--white);font-size:16px;line-height:23px}
.cta-copy p{margin-bottom:19px}

/* footer */
.footer-brand{left:0;top:3996px;width:1200px;text-align:center;font-size:19px;font-weight:500;color:var(--ink)}
.footer-dot{left:556px;top:3984px;width:44px;height:44px;border-radius:50%;background:var(--green);opacity:.35}
.fine{top:4087px;font-size:9.5px;color:var(--body)}
</style>
</head>
<body>

<!-- hero -->
<svg class="abs hero-photo" viewBox="0 0 1200 520" role="img" aria-label="Photo of two smiling businessmen looking at a laptop in a bright office">
  <defs>
    <linearGradient id="heroFill" x1="0" y1="0" x2="1" y2="1">
      <stop offset="0" stop-color="#6aa7c4"/>
      <stop offset=".5" stop-color="#3d7ea3"/>
      <stop offset="1" stop-color="#8fb6a8"/>
    </linearGradient>
    <linearGradient id="heroEdge" x1="0" y1="0" x2="1" y2="1">
      <stop offset="0" stop-color="#34a6d7"/>
      <stop offset="1" stop-color="#abd036"/>
    </linearGradient>
  </defs>
  <path d="M760,0 C705,70 680,170 722,262 C775,370 880,470 1000,495 C1090,512 1160,472 1200,420 L1200,0 Z" fill="url(#heroFill)" stroke="url(#heroEdge)" stroke-width="9"/>
</svg>
<div class="abs brand">GuideLink Hub</div>
<div class="btn" style="left:862px;top:32px;width:123px;height:30px">Find my Mentor</div>
<h1 class="abs hero-title">A Mentor for Everyone</h1>
<div class="abs hero-sub">Free Registration. 100% Confidential.&nbsp; 100% Obligation Free</div>
<div class="btn" style="left:211px;top:317px;width:151px;height:37px">Find my Mentor</div>

<!-- quote -->
<p class="abs quote">"We've flipped the model on its head - &nbsp;so now you choose your Mentor.&nbsp; It's never been this easy to get the advice and guidance you need to thrive"</p>
<div class="abs quote-by">Oliver, Founder - GuideLink Hub</div>

<!-- intro -->
<h2 class="section-title" style="top:738px">Finding a Mentor Has Never Been Easier</h2>
<div class="rule" style="top:787px"></div>
<svg class="abs intro-blob" viewBox="0 0 330 295" role="img" aria-label="Soft overlapping colour washes in blue and green">
  <defs>
    <radialGradient id="wash" cx=".5" cy=".5" r=".5">
      <stop offset="0" stop-color="#abd036" stop-opacity=".55"/>
      <stop offset=".7" stop-color="#8cc27a" stop-opacity=".45"/>
      <stop offset="1" stop-color="#34a6d7" stop-opacity="0"/>
    </radialGradient>
  </defs>
  <ellipse cx="165" cy="148" rx="165" ry="147" fill="url(#wash)"/>
</svg>
<div class="abs intro-copy">
  <p>Having a great Mentor will turbo-charge your personal, professional or business growth.&nbsp; But unless you have an incredible network, finding great Mentors has always been a challenge.</p>
  <p>GuideLink Hub changes all that, levelling the playing field and making it easy for entrepreneurs and professionals to find the advice and guidance they deserve.</p>
  <p>No longer will you have to go searching for your perfect Mentor.&nbsp; We bring the perfect Mentor to you, selected from a global pool of experts, putting the power back in your hands and letting you get on with your growth.</p>
</div>

<!-- steps -->
<h2 class="section-title" style="top:1206px">Mentorship: But Different</h2>
<div class="rule" style="top:1256px"></div>
<p class="abs lead">Finding a Mentor used to be hard; but not any more. We've turned the traditional model on its head, so now Mentors seek you</p>

<svg class="abs" style="left:370px;top:1388px;width:460px;height:80px" viewBox="0 0 460 80" aria-hidden="true">
  <g fill="none" stroke="#555" stroke-width="1.3" stroke-dasharray="4 4">
    <path d="M12,68 C60,30 130,20 180,62"/>
    <path d="M277,68 C325,30 395,20 445,62"/>
  </g>
  <g fill="#555"><path d="M180,62 l-8,-2 l4,-5 z"/><path d="M445,62 l-8,-2 l4,-5 z"/></g>
  <path d="M75,8 L102,12 L82,24 Z" fill="#34a6d7"/><path d="M75,8 L88,16 L82,24 Z" fill="#abd036"/>
  <path d="M340,8 L367,12 L347,24 Z" fill="#34a6d7"/><path d="M340,8 L353,16 L347,24 Z" fill="#abd036"/>
</svg>

<div class="step" style="left:228px">
  <h3>Tell Us What You Need</h3>
  <p>There is no one size fits all approach to Mentorship.&nbsp; So tell us the challenges you are facing and the skill-set your Mentor must have.</p>
</div>
<div class="step" style="left:490px">
  <h3>Choose Your Mentor</h3>
  <p>Mentors are invited to Mentor you. We select 3 top picks that align with your criteria.&nbsp; It's then up to you whether you choose a Mentor, interview 1 or more or refine your criteria and start again.</p>
</div>
<div class="step" style="left:753px">
  <h3>Ongoing Support</h3>
  <p>We don't stop once you have your perfect Mentor.&nbsp; We're on hand to make life easy for you, keep your sessions on track and provide ongoing support.</p>
</div>
<div class="btn" style="left:525px;top:1722px;width:149px;height:35px">Find my Mentor</div>

<!-- benefits -->
<div class="abs benefits" role="img" aria-label="Photo of two men in a meeting beside large office windows, tinted blue to green"></div>
<h2 class="abs benefits-title">How a Mentor Will Accelerate Your Growth</h2>
<div class="rule" style="top:2001px;background:var(--white)"></div>

<div class="benefit" style="left:231px;top:2062px">
  <svg viewBox="0 0 44 44" fill="none" stroke="#fff" stroke-width="1.6"><circle cx="17" cy="16" r="8"/><path d="M6,38 c0-8 5-12 11-12 s11,4 11,12 z"/><path d="M30,10 q4,6 0,12 M34,7 q6,9 0,18"/></svg>
  <h3>Impartial advice</h3><span class="rule"></span>
  <p>Imagine being able to speak to someone who has been through the challenges you are currently facing?&nbsp; Who has 'been there seen that' and can help you navigate the ups and downs of your career or business?</p>
</div>
<div class="benefit" style="left:493px;top:2062px">
  <svg viewBox="0 0 44 44" fill="none" stroke="#fff" stroke-width="1.6"><rect x="7" y="16" width="12" height="20" rx="4"/><rect x="25" y="16" width="12" height="20" rx="4"/><path d="M19,22 h6 M10,16 v-8 h6 v8 M28,16 v-8 h6 v8"/></svg>
  <h3>Avoid the Pitfalls</h3><span class="rule"></span>
  <p>An experienced Mentor will help you see the challenges before they arise and make sure you avoid them altogether. Saving valuable time and money in the process.</p>
</div>
<div class="benefit" style="left:756px;top:2062px">
  <svg viewBox="0 0 44 44" fill="none" stroke="#fff" stroke-width="1.6"><path d="M16,18 a9,9 0 1 1 16,6 c-3,3 -5,5 -5,9 a5,5 0 0 1 -9,2"/><path d="M21,19 a3,3 0 1 1 5,3"/><path d="M9,14 q-3,5 0,10"/></svg>
  <h3>A Supportive Ear</h3><span class="rule"></span>
  <p>Running a business and the challenges of corporate life can be extremely stressful.&nbsp; And often, our friends and family just don't get it.&nbsp; So imagine having someone independent who can understand where your coming from and, help you see things objectively.</p>
</div>

<div class="benefit" style="left:231px;top:2325px">
  <svg viewBox="0 0 44 44" fill="none" stroke="#fff" stroke-width="1.6"><circle cx="22" cy="22" r="16"/><path d="M8,18 c6,2 8,-4 14,-2 s4,8 10,6 M12,32 c4,-4 10,-2 12,-6 M22,6 c-3,5 2,8 0,12"/></svg>
  <h3>Clarity</h3><span class="rule"></span>
  <p>Sometimes we are so caught up in our own world we struggle to see the big picture.&nbsp; Your Mentor will provide an objective, outsider view.&nbsp; Helping you to cut though the noise and focus on what's really important.</p>
</div>
<div class="benefit" style="left:493px;top:2325px">
  <svg viewBox="0 0 44 44" fill="none" stroke="#fff" stroke-width="1.6"><circle cx="22" cy="9" r="4"/><path d="M22,13 v12 M12,20 l10,4 l10,-4 M8,34 q14,-10 28,0 M10,38 h24"/></svg>
  <h3>Motivation</h3><span class="rule"></span>
  <p>Your Mentor has seen this before and been in your shoes.&nbsp; They understand what your going through and will help you to re-focus and re-energise.</p>
</div>
<div class="benefit" style="left:756px;top:2325px">
  <svg viewBox="0 0 44 44" fill="none" stroke="#fff" stroke-width="1.6"><path d="M15,6 v34 M29,6 v34 M15,12 h14 M15,19 h14 M15,26 h14 M15,33 h14"/><circle cx="22" cy="5" r="2.5"/></svg>
  <h3>Make you Accountable</h3><span class="rule"></span>
  <p>A Mentor is not just there to pick you up - they are to give honest appraisal and tell you when your falling short.&nbsp; Ultimately, only you can control your success and you Mentor will hold you accountable to make sure you are.</p>
</div>
<div class="btn" style="left:525px;top:2576px;width:149px;height:34px">Find my Mentor</div>

<!-- faq -->
<h2 class="section-title" style="top:2735px">Frequently Asked Questions</h2>
<div class="rule" style="top:2786px"></div>

<div class="faq-item active" style="top:2877px">What is a Mentor?</div>
<div class="faq-item" style="top:2936px">Is a Mentor right for me?</div>
<div class="faq-item" style="top:2995px">How often do we meet?</div>
<div class="faq-item" style="top:3054px">Can I have more than one Mentor?</div>
<div class="faq-item" style="top:3113px">What if it doesn't work out?</div>
<div class="faq-item" style="top:3172px">How do we meet?</div>
<div class="faq-item" style="top:3231px">What are the costs?</div>

<div class="abs faq-answer">
  <p>Experienced and Trusted Advisor.&nbsp; Guru. Confidente.&nbsp; Friend.</p>
  <p>In essence a Mentor is someone who can turn to for guidance and advice.</p>
  <p>Someone who is more experienced than you and, has navigated similar challenges to you and can foresee the pitfalls and hurdles you face.</p>
  <p>A great Mentor is also a motivator, connector and guide.&nbsp; Will help you focus on what's really important and see the bigger picture.</p>
  <p>Importantly, a great Mentor should be outside your immediate network of friends and relatives. And, be able to offer unbiased, honest and objective advice, that you can action.</p>
</div>

<!-- cta -->
<div class="abs cta" role="img" aria-label="Photo of a relaxed workspace, tinted green to blue"></div>
<h2 class="abs cta-title">It's Time to Invest in You</h2>
<div class="rule" style="top:3582px;background:var(--green)"></div>
<div class="abs cta-copy">
  <p>If you've come this far you've already taken the most important step: recognising how mentorship can help you; and taking action to find it.</p>
  <p>And now your here, the rest is easy.</p>
  <p>Get started now and let GuideLink Hub do the rest...</p>
</div>
<div class="btn" style="left:525px;top:3819px;width:149px;height:35px">Let`s Do This</div>

<!-- footer -->
<div class="abs footer-dot"></div>
<div class="abs footer-brand">GuideLink Hub</div>
<div class="abs fine" style="left:211px">© 2018 GuideLinkHub. All Rights Reserved.</div>
<div class="abs fine" style="left:700px;width:288px;text-align:right">Sign up is free, obligation free and 100% confidential.</div>

</body>
</html>
```